Fahrzeugbeschriftung für Elektrotechnik-Betrieb
Zielgruppe
Unser Kunde ist ein Heizung und Sanitär Betrieb mit Sitz in Hamburg. Zu uns kamen sie mit dem Wunsch nach einer Webseite für Ihren Imageaufbau und Mitarbeitersuche. Der Meisterbetrieb beschäftigt sich mit Heizung und hochwertigen exklusiven Bädern.
Die Domain der aktuellen Webseite: brunner-waerme.de
Adresse: Holderbachweg 14, 54528 Kastelheim
Telefonnummer: 06573 817360
Bitte das Design beachten, sonst gerne kreativ und auffällig! Im Vordergrund stehen die zwei Themenbereiche Bäder und Heizung und zusätzlich die Mitarbeitersuche. Beispielbilder im Anhang! (Das alte Autodesign befindet sich auch im Anhang)
Aufgabenstellung
Der Kunde hätte das Autodesign gerne auffällig und modern. Im Fokus stehen die Leistungen (Heizung und Bäder) und die Mitarbeitersuche. Ebenfalls sollen Logo (befindet sich im Anhang), Telefonnummer und Webseite klar zu sehen sein.
Nähere Vorgaben:
-Vorne: nur das Logo
-Seiten: Thema Bad und Heizung, Aufruf zur Mitarbeitersuche, Logo, Telefonnummer, Webseite
-Hinten: Logo (groß/oben); Telefonnummer und Webseite (rechts), Aufruf zur Mitarbeitersuche (links)
Unsere Idee: Aufteilung der Themen Bäder und Heizung
1. auf der einen Seite des Autos Thema “Bäder”(blau aus Logo) - Der Kunde möchte hochwertige Bäder verkaufen!
Bsp.:“Dein Partner rund um deine exklusive Wellnessoase”
Mitarbeitersuche: “Bei uns fühlst auch du dich wohl/Nicht nur die Kunden fühlen sich bei uns wohl. Bewirb dich jetzt! “
Bitte mit Bildern arbeiten! Ein schönes Badezimmer mit lächelnden Menschen. Stockfotos bitte passend farblich anpassen.
Beispiel Stockfotos:
- https://www.bildarchivplus.example/de/image-photo/happy-laughing-asian-woman-shaving-her-100000001
- https://www.bildarchivplus.example/de/image-photo/portrait-young-happy-couple-getting-ready-100000002
- https://www.bildarchivplus.example/de/image-photo/couple-facing-bathroom-drawing-gradating-photo-100000003
- https://www.bildarchivplus.example/de/image-photo/morning-sexy-couple-muscular-man-bath-100000004
2. und auf der anderen Seite Thema “Heizung”(orange aus Logo)
Bsp.:“Wir sorgen auch für dein perfektes Wohlfühlklima”
Mitarbeitersuche: “Bei uns fühlst auch du dich wohl/Nicht nur die Kunden fühlen sich bei uns wohl. Bewirb dich jetzt!”
Bitte mit Bildern arbeiten! Ein passendes Bild mit fröhlicher Familie. Stockfotos bitte passend farblich anpassen.
- https://www.bildarchivplus.example/de/image-photo/floor-heating-young-woman-walking-house-100000005
- https://www.bildarchivplus.example/de/image-illustration/heating-concept-un..

```html
<!DOCTYPE html>
<html lang="de">
<head>
<meta charset="utf-8">
<title>brunner haustechnik – Fahrzeugbeschriftung</title>
<link href="https://fonts.googleapis.com/css2?family=Pathway+Gothic+One&family=Varela+Round&family=Mr+Dafoe&display=swap" rel="stylesheet">
<style>
  :root{
    --bg:#f2f2f2;
    --panel:#ffffff;
    --ink:#3f3f3f;
    --teal:#1fa3b5;
    --orange:#ef7d28;
    --trim:#1d1d1d;
  }
  *{box-sizing:border-box;margin:0;padding:0}
  html,body{width:1200px;height:960px;overflow:hidden;background:var(--bg)}
  body{position:relative;font-family:"Varela Round",sans-serif;color:var(--ink)}

  .surface{position:absolute;background:var(--panel);border-radius:18px 18px 6px 6px;overflow:hidden;box-shadow:0 14px 24px rgba(0,0,0,.12)}
  .trim{position:absolute;left:0;right:0;bottom:0;background:var(--trim)}

  .brand{position:absolute;display:flex;align-items:center;gap:10px}
  .brand-mark{background:var(--orange);flex:none}
  .brand-name{font-family:"Pathway Gothic One",sans-serif;color:var(--ink);line-height:.95;letter-spacing:.5px;white-space:nowrap}

  .claim{position:absolute;font-family:"Pathway Gothic One",sans-serif;color:var(--ink);line-height:1.2;white-space:nowrap}
  .call{position:absolute;font-family:"Mr Dafoe",cursive;white-space:nowrap;line-height:1}
  .call--teal{color:var(--teal)}
  .call--orange{color:var(--orange)}
  .call--dark{color:var(--ink)}

  .contact{position:absolute;font-size:10px;line-height:1.35;white-space:nowrap}
  .web{position:absolute;font-size:12px;letter-spacing:.3px;white-space:nowrap}

  .photo{position:absolute;border-radius:50%;border:4px solid var(--teal)}
  .photo--orange{border-color:var(--orange)}

  .back{left:80px;top:150px;width:380px;height:270px}
  .side-bath{left:510px;top:150px;width:620px;height:230px}
  .front{left:80px;top:520px;width:380px;height:250px}
  .side-heat{left:510px;top:520px;width:620px;height:230px}
</style>
</head>
<body>

<!-- Rear doors -->
<section class="surface back">
  <div class="brand" style="left:105px;top:22px">
    <span class="brand-mark" style="width:44px;height:44px"></span>
    <span class="brand-name" style="font-size:32px">brunner<br>haustechnik</span>
  </div>
  <p class="call call--dark" style="left:30px;top:108px;font-size:32px;transform:rotate(-8deg)">Bewirb Dich Jetzt!</p>
  <div class="contact" style="left:215px;top:168px;font-size:9px">tel : 06573 817360</div>
  <div class="web" style="left:215px;top:182px;font-size:11px">www.brunner-waerme.de</div>
  <div class="trim" style="height:52px"></div>
</section>

<!-- Driver side: baths -->
<section class="surface side-bath">
  <p class="claim" style="left:22px;top:18px;font-size:15px">Bei uns fühlst auch du dich wohl/Nicht<br>nur die Kunden fühlen sich bei uns wohl</p>
  <p class="call call--teal" style="left:60px;top:56px;font-size:24px">Bewirb Dich Jetzt!</p>
  <div class="photo" role="img" aria-label="Installateur berät ein Paar im Badezimmer" style="left:-6px;top:90px;width:104px;height:104px;background:linear-gradient(135deg,#c9d4dc,#6d7f90)"></div>
  <div class="photo" role="img" aria-label="Lachendes Paar in einem hellen Designbad" style="left:80px;top:92px;width:104px;height:104px;background:linear-gradient(135deg,#eee7df,#b98f73)"></div>
  <div class="photo" role="img" aria-label="Entspannte Frau in der Badewanne" style="left:162px;top:110px;width:96px;height:96px;background:linear-gradient(135deg,#f4efe8,#d8c2ad)"></div>
  <div class="brand" style="left:300px;top:28px">
    <span class="brand-mark" style="width:40px;height:40px;background:var(--teal)"></span>
    <span class="brand-name" style="font-size:32px">brunner<br>haustechnik</span>
  </div>
  <div class="contact" style="left:480px;top:122px">Holderbachweg 14,<br>54528 Kastelheim<br>tel : 06573 817360</div>
  <div class="web" style="left:268px;top:164px">www.brunner-waerme.de</div>
  <div class="trim" style="height:22px"></div>
</section>

<!-- Front -->
<section class="surface front">
  <div class="brand" style="left:120px;top:58px">
    <span class="brand-mark" style="width:32px;height:32px"></span>
    <span class="brand-name" style="font-size:24px">brunner<br>haustechnik</span>
  </div>
  <div class="trim" style="height:110px;border-radius:30px 30px 0 0"></div>
</section>

<!-- Passenger side: heating -->
<section class="surface side-heat">
  <div class="brand" style="left:200px;top:34px">
    <span class="brand-mark" style="width:40px;height:40px"></span>
    <span class="brand-name" style="font-size:32px">brunner<br>haustechnik</span>
  </div>
  <p class="claim" style="left:395px;top:18px;font-size:15px">Bei uns fühlst auch du dich wohl/Nicht<br>nur die Kunden fühlen sich bei uns wohl</p>
  <p class="call call--orange" style="left:410px;top:56px;font-size:24px">Bewirb Dich Jetzt!</p>
  <div class="photo photo--orange" role="img" aria-label="Barfüße auf warmem Holzboden mit Fußbodenheizung" style="left:392px;top:112px;width:96px;height:96px;background:linear-gradient(135deg,#b9c6d1,#9a6a45)"></div>
  <div class="photo photo--orange" role="img" aria-label="Raumthermostat vor Heizungsrohren" style="left:480px;top:98px;width:96px;height:96px;background:linear-gradient(135deg,#e9e4de,#b78a63)"></div>
  <div class="contact" style="left:40px;top:128px">Holderbachweg 14,<br>54528 Kastelheim<br>tel : 06573 817360</div>
  <div class="web" style="left:200px;top:164px">www.brunner-waerme.de</div>
  <div class="trim" style="height:22px"></div>
</section>

</body>
</html>
```